Landing page for Dunmore Aviation

Re-design the landing page for www.dunmoreaviation-example.com. It needs to be flatter and work with both PC, Mac and Mobile. Sites I like are as follows:
http://kravelaero-example.com
http://zuvair-example.com
http://www.skyvantor-example.com
http://www.bralojet-example.com/bjc.php
http://www.qwing-example.com
http://www.tolvenair-example.com
http://www.merrowfieldaerohub-example.com
http://www.corvexwings-example.com
http://www.stratovelfield-example.com

We are a Durnell 48 Dealer, SkyVesta FBO member, Kestrin Circle FBO, TQN Preferred FBO located only 6 miles from Downtown Atlanta. Providing Aircraft charter, Aircraft sales, Aircraft Maintenance, Aircraft Line Services and Hangar, and Parts Support.
Updates

Project Deadline Extended
Reason: I have six people reviewing designs within the company and will not be able to complete the review until next week.

Target Market(s)

Pilot's looking for a place to take care of them in Atlanta

Industry/Entity Type

Group

Colors
fbed22
0555a3

Requirements
Must have
• Slogan "Focused on Arrival" and "Sensational Southern Service"

```html
<!DOCTYPE html>
<html lang="en">
<head>
<meta charset="utf-8">
<title>Dunmore Aviation &amp; Leasing</title>
<link href="https://fonts.googleapis.com/css2?family=Oswald:wght@300;400;500&family=Noto+Serif:wght@400;700&display=swap" rel="stylesheet">
<style>
:root{
  --yellow:#fbed22;
  --blue:#0555a3;
  --ink:#111;
  --text:#555;
  --muted:#888;
  --rule:#dcdcdc;
  --tile:#efefef;
}
*{box-sizing:border-box;margin:0;padding:0}
html,body{width:799px;height:1200px;overflow:hidden;background:#fff}
body{position:relative;font-family:"Noto Serif",Georgia,serif;color:var(--text)}
.abs{position:absolute}
.topbar{left:0;top:0;width:799px;height:17px;border-bottom:1px solid var(--rule)}
.topbar .date{left:71px;top:3px;font-size:9px;color:var(--muted)}
.topbar .phones{right:66px;top:3px;font-size:9px;color:var(--muted);display:flex;gap:12px;align-items:center}
.brand{left:66px;top:34px;display:flex;align-items:center;gap:8px;font-family:"Oswald",sans-serif;font-size:20px;font-weight:400;color:var(--blue)}
.brand .mark{width:18px;height:18px;background:var(--yellow)}
.tagline{left:92px;top:64px;font-family:"Oswald",sans-serif;font-weight:300;font-size:10px;letter-spacing:1.5px;color:var(--blue);text-transform:uppercase}
.social{top:22px;width:22px;height:22px;border-radius:50%;border:1.5px solid var(--blue)}
.clock{top:52px;width:48px;height:32px;background:var(--tile);font-family:"Oswald",sans-serif;font-weight:300;font-size:8.5px;padding:4px 0 0 8px;line-height:12px;white-space:nowrap;overflow:hidden}
.clock .city{color:var(--blue)}
.clock .time{color:var(--text)}
.nav{left:66px;top:90px;width:667px;height:31px;border-top:1px solid var(--rule);display:flex;justify-content:space-between;align-items:center;padding:0 9px;font-family:"Oswald",sans-serif;font-weight:300;font-size:11.5px;color:var(--ink);text-transform:uppercase}
.nav .active{color:var(--blue)}
.hero{left:66px;top:122px;width:667px;height:274px;overflow:hidden;
  background:
   radial-gradient(ellipse 70% 40% at 55% 52%,rgba(255,250,235,.55),rgba(255,250,235,0) 70%),
   linear-gradient(180deg,#9fb0bc 0%,#c9ccc6 30%,#e6dcc4 48%,#b9ad93 58%,#6c6658 66%,#3d3d3f 78%,#2a2b2e 100%)}
.hero .slogan{left:39px;top:218px;font-family:"Oswald",sans-serif;font-weight:500;font-size:19px;line-height:20px;color:var(--yellow);letter-spacing:.4px}
.hero .bar{left:0;top:239px;width:667px;height:3px;background:var(--yellow)}
.dot{top:250px;width:15px;height:15px;border-radius:50%;border:2px solid #bbb}
.dot.on{border-color:var(--yellow)}
.photo{background:radial-gradient(circle at 35% 30%,#d8c8a8 0%,#a08a6c 40%,#5f4d3c 100%)}
h2.title{font-family:"Oswald",sans-serif;font-weight:400;color:var(--ink)}
.welcome h2{left:237px;top:428px;font-size:20px;line-height:28px;white-space:nowrap}
.welcome p{left:237px;width:326px;font-size:8px;line-height:15px}
.btn{width:97px;height:24px;border:1.5px solid var(--ink);font-family:"Oswald",sans-serif;font-size:8.5px;color:var(--ink);display:flex;align-items:center;justify-content:center;text-transform:uppercase}
.rule{height:1px;background:var(--rule)}
.section-h{font-family:"Oswald",sans-serif;font-size:14px;color:var(--ink)}
.news-date{left:66px;font-size:7.5px;color:var(--muted)}
.news-thumb{left:66px;width:40px;height:40px;background:radial-gradient(circle at 50% 35%,#d9c9b6,#8b7664 60%,#4d4036)}
.news-text{left:114px;width:108px;font-size:7.5px;line-height:11px;color:var(--text)}
.video{left:237px;top:617px;width:325px;height:231px;background:var(--yellow)}
.video h3{left:8px;top:6px;font-family:"Oswald",sans-serif;font-weight:400;font-size:12.5px;color:var(--ink);white-space:nowrap}
.video .hint{left:8px;top:24px;font-size:8.5px;color:#333}
.screen{left:8px;top:46px;width:269px;height:177px;background:#000;color:#fff;text-align:center}
.screen .name{left:0;top:48px;width:269px;font-family:"Oswald",sans-serif;font-size:18px;color:var(--yellow)}
.screen .cap{left:0;top:108px;width:269px;font-size:12px;line-height:17px}
.play{left:288px;top:196px;width:26px;height:26px}
.fbo-h{left:66px;top:880px}
.fbo-sub{left:66px;top:898px;font-size:9.5px;color:var(--blue)}
.fbo-list{left:66px;top:918px;list-style:none;font-size:8.5px;line-height:15px}
.fbo-list li::before{content:"";display:inline-block;width:4px;height:4px;border-radius:50%;background:var(--blue);margin:0 7px 1px 1px}
.interior{background:radial-gradient(ellipse at 30% 40%,#e3d4b6 0%,#b9a78a 35%,#6c7688 80%,#4a5365 100%)}
.svc-h{left:579px;top:427px}
.svc-img{left:579px;width:154px;height:96px}
.svc-label{left:579px;font-size:10px;color:var(--blue)}
.badge{top:1120px;height:38px}
.badge.box{border:1px solid var(--rule);background:#fff}
.badge.box span{position:absolute;left:50%;top:50%;width:22px;height:10px;transform:translate(-50%,-50%);background:#c9d3de}
.footer{left:0;top:1174px;width:799px;height:26px;background:var(--blue);color:#fff;font-size:8px;display:flex;align-items:center;justify-content:center}
</style>
</head>
<body>

<header>
  <div class="abs topbar">
    <div class="abs date">Friday March 28, 2014</div>
    <div class="abs phones">
      <svg width="11" height="9" viewBox="0 0 11 9"><rect x="1" y="3" width="9" height="6" rx="1" fill="var(--blue)"/><rect x="0" y="0" width="11" height="3" rx="1.5" fill="var(--blue)"/></svg>
      <span>404-555-0142</span><span>800-555-0187</span>
    </div>
  </div>

  <div class="abs brand"><span class="mark"></span>Dunmore Aviation</div>
  <div class="abs tagline">Focused on Arrival</div>

  <div class="abs social" style="left:627px"></div>
  <div class="abs social" style="left:655px"></div>
  <div class="abs social" style="left:683px"></div>
  <div class="abs social" style="left:711px"></div>

  <div class="abs clock" style="left:400px"><div class="city">Atlanta</div><div class="time">07:56:36</div></div>
  <div class="abs clock" style="left:457px"><div class="city">GMT</div><div class="time">07:56:36</div></div>
  <div class="abs clock" style="left:514px"><div class="city">San Francisco</div><div class="time">07:56:36</div></div>
  <div class="abs clock" style="left:571px"><div class="city">Salt Lake</div><div class="time">07:56:36</div></div>
  <div class="abs clock" style="left:628px"><div class="city">Dallas</div><div class="time">07:56:36</div></div>
  <div class="abs clock" style="left:685px"><div class="city">London</div><div class="time">07:56:36</div></div>

  <nav class="abs nav">
    <span class="active">Home</span><span>About Us</span><span>Aircraft Management</span><span>Charter</span><span>FBO Services</span><span>Maintenance</span><span>Aircraft Parts</span><span>Aircraft Sales</span><span>Resources</span><span>Contact Us</span>
  </nav>
</header>

<section class="abs hero" role="img" aria-label="Business jet parked on the ramp at sunset">
  <div class="abs slogan">Sensational Southern Service</div>
  <div class="abs bar"></div>
  <div class="abs dot on" style="left:605px"></div>
  <div class="abs dot" style="left:623px"></div>
  <div class="abs dot" style="left:641px"></div>
</section>

<section class="welcome">
  <div class="abs photo" style="left:66px;top:431px;width:154px;height:152px" role="img" aria-label="Customer service representative at the front desk"></div>
  <h2 class="abs title">Welcome to Dunmore Aviation &amp; Leasing</h2>
  <p class="abs" style="top:463px">Atlanta's Most Established Fixed Based Operation established in 1955 by Southern Aviation Hall of Fame member Everett Dunmore, Sr.</p>
  <p class="abs" style="top:498px">Our world class FBO facilities offer all the amenities for passengers and pilots, including computer work stations with internet access, plasma TV for catching up on national and world events, pilots lounge with theatre seating...</p>
  <div class="abs btn" style="left:237px;top:558px">Read More</div>
</section>

<div class="abs rule" style="left:66px;top:600px;width:496px"></div>

<section class="news">
  <div class="abs section-h" style="left:66px;top:623px">Latest News</div>
  <div class="abs rule" style="left:66px;top:646px;width:154px"></div>

  <div class="abs news-date" style="top:653px">12.03.2014</div>
  <div class="abs news-thumb" style="top:668px" role="img" aria-label="Award presentation"></div>
  <div class="abs news-text" style="top:665px">Dunmore Aviation &amp; Leasing Corp., Receives 50 Year Safe Flying Award at NAVA 60th....</div>

  <div class="abs news-date" style="top:723px">12.03.2014</div>
  <div class="abs news-thumb" style="top:738px" role="img" aria-label="Chief pilot portrait"></div>
  <div class="abs news-text" style="top:735px">Dale Corwin, Chief Pilot for Dunmore Aviation has been named as primary</div>

  <div class="abs news-date" style="top:793px">12.03.2014</div>
  <div class="abs news-thumb" style="top:808px" role="img" aria-label="Chief pilot portrait"></div>
  <div class="abs news-text" style="top:805px">Dale Corwin, Chief Pilot for Dunmore Aviation has been named as primary</div>
</section>

<section class="abs video">
  <h3 class="abs">Dunmore Aviation: Legendary Company Celebrates Fifty Years</h3>
  <div class="abs hint">Position cursor over the video to activate playback controls.</div>
  <div class="abs screen">
    <div class="abs name">Dunmore Aviation</div>
    <div class="abs cap">Celebrating 50 Years of<br>Family, Friends and Good Business</div>
  </div>
  <svg class="abs play" viewBox="0 0 26 26"><circle cx="13" cy="13" r="11.5" fill="none" stroke="#111" stroke-width="2"/><path d="M11 8l5 5-5 5" fill="none" stroke="#111" stroke-width="2"/></svg>
</section>

<div class="abs rule" style="left:66px;top:866px;width:496px"></div>

<section class="fbo">
  <div class="abs section-h fbo-h">FBO Services</div>
  <div class="abs fbo-sub">Services, Facilities &amp; Amenities</div>
  <ul class="abs fbo-list">
    <li>Aviation fuel</li>
    <li>Aircraft parking (ramp or tiedown)</li>
    <li>Hangars</li>
    <li>Passenger terminal and lounge</li>
    <li>Aircraft charters</li>
    <li>Aircraft maintenance</li>
    <li>Avionics sales and service</li>
    <li>Aircraft interiors</li>
    <li>Aircraft parts</li>
  </ul>
  <div class="abs btn" style="left:66px;top:1060px">Read More</div>

  <div class="abs interior" style="left:237px;top:882px;width:219px;height:97px" role="img" aria-label="Passenger lounge"></div>
  <div class="abs interior" style="left:465px;top:882px;width:97px;height:97px;background:radial-gradient(ellipse at 50% 40%,#e7dcc6,#a79a88 45%,#5a6272)" role="img" aria-label="Snack area"></div>
  <div class="abs interior" style="left:237px;top:988px;width:97px;height:97px;background:radial-gradient(ellipse at 40% 35%,#efe6d2,#bba78a 50%,#6b5a48)" role="img" aria-label="Pilot at the front counter"></div>
  <div class="abs interior" style="left:343px;top:988px;width:219px;height:97px;background:radial-gradient(ellipse at 60% 40%,#e6d8bd,#a3774f 50%,#4e3a2c)" role="img" aria-label="Computer work stations"></div>
</section>

<aside class="services">
  <div class="abs section-h svc-h">Our Services</div>
  <div class="abs rule" style="left:579px;top:451px;width:154px;background:#bbb"></div>

  <div class="abs svc-img" style="top:461px;background:radial-gradient(ellipse at 50% 45%,#f2f2f0,#c8cfd6 40%,#7f8578 100%)" role="img" aria-label="Line service crew with a jet"></div>
  <div class="abs svc-label" style="top:562px">Aircraft Line Services</div>

  <div class="abs svc-img" style="top:590px;background:radial-gradient(ellipse at 50% 55%,#eceded,#b9bbbd 45%,#6d7073 100%)" role="img" aria-label="Jets parked in the hangar"></div>
  <div class="abs svc-label" style="top:691px">Hangar</div>

  <div class="abs svc-img" style="top:719px;background:radial-gradient(ellipse at 70% 40%,#eef0f2,#b7bcc3 40%,#4f5663 100%)" role="img" aria-label="Engine maintenance in the shop"></div>
  <div class="abs svc-label" style="top:820px">Parts Support</div>

  <div class="abs svc-img" style="top:848px;background:radial-gradient(ellipse at 45% 60%,#c7cfd9,#5b6a7d 45%,#1c2a3e 100%)" role="img" aria-label="Jet on the ramp at dusk"></div>
  <div class="abs svc-label" style="top:949px">Aircraft Sales</div>

  <div class="abs svc-img" style="top:977px;background:radial-gradient(ellipse at 45% 60%,#c7cfd9,#5b6a7d 45%,#1c2a3e 100%)" role="img" aria-label="Jet ready for charter"></div>
  <div class="abs svc-label" style="top:1076px">Aircraft Charter</div>
</aside>

<div class="abs rule" style="left:66px;top:1103px;width:667px"></div>

<section class="partners">
  <div class="abs badge" style="left:66px;width:69px;background:#bcd6ee;border-radius:4px"></div>
  <div class="abs badge" style="left:153px;width:45px;background:#dbe7c9;border-radius:4px"></div>
  <div class="abs badge" style="left:216px;top:1127px;width:95px;height:24px;background:#e3e6ea"></div>
  <div class="abs badge box" style="left:342px;width:47px"><span></span></div>
  <div class="abs badge box" style="left:399px;width:47px"><span></span></div>
  <div class="abs badge box" style="left:456px;width:47px"><span></span></div>
  <div class="abs badge box" style="left:513px;width:47px"><span></span></div>
  <div class="abs badge box" style="left:570px;width:47px"><span></span></div>
  <div class="abs badge box" style="left:627px;width:47px"><span></span></div>
  <div class="abs badge box" style="left:684px;width:49px"><span></span></div>
</section>

<footer class="abs footer">©2014 Dunmore Aviation &amp; Leasing All Rights Reserved</footer>

</body>
</html>
```